Business Card Design Project

In addition to the logo design we want a professional and contemporary business card for a talent management agency. We provide management services to creative artists and want to communicate a professional creative vibe.
Updates

Reason: Sorry didnt realise I had put such a short timeline on it.

Target Market(s)

The business deals with creative artists and other industry professionals

Industry/Entity Type

Artists

Colors

Designer to choose colors to be used in the design.

Requirements
Must have
• Logo
Address
Phone
Email

```html
<!DOCTYPE html>
<html lang="en">
<head>
<meta charset="utf-8">
<title>Kestrel Artists – Business Card</title>
<link href="https://fonts.googleapis.com/css2?family=Arimo:wght@400;700&display=swap" rel="stylesheet">
<style>
  :root {
    --canvas-bg: #e9e7e4;
    --card-white: #ffffff;
    --brand-green: #1c5a33;
    --card-black: #121212;
    --text-light: #f2f2f2;
  }
  * { box-sizing: border-box; margin: 0; padding: 0; }
  html, body {
    width: 1200px; height: 960px; overflow: hidden;
    background: var(--canvas-bg);
    font-family: "Arimo", Arial, sans-serif;
  }
  .canvas {
    width: 1200px; height: 960px;
    display: flex; flex-direction: column; align-items: center; justify-content: center;
    gap: 40px;
  }
  .card {
    position: relative;
    width: 700px; height: 400px;
    border-radius: 18px;
    overflow: hidden;
    background: var(--card-white);
    box-shadow: 0 6px 18px rgba(0,0,0,0.15);
  }
  .wordmark {
    color: var(--brand-green);
    font-weight: 700;
    line-height: 0.95;
    letter-spacing: -0.5px;
  }
  .wordmark span { display: block; }

  /* Front */
  .card-front .wordmark {
    position: absolute; right: 52px; bottom: 64px;
    font-size: 58px; text-align: left;
  }

  /* Back */
  .card-back .top-panel {
    position: absolute; left: 0; top: 0; right: 0; height: 222px;
    background: var(--card-white);
  }
  .card-back .wordmark {
    position: absolute; left: 44px; top: 92px;
    font-size: 58px;
  }
  .holder {
    position: absolute; right: 48px; top: 44px;
    color: var(--brand-green);
  }
  .holder-name { font-size: 24px; font-weight: 700; }
  .holder-role { font-size: 15px; font-weight: 400; margin-top: 2px; }
  .accent-stripe {
    position: absolute; left: 0; right: 0; top: 222px; height: 10px;
    background: var(--brand-green);
  }
  .bottom-panel {
    position: absolute; left: 0; right: 0; top: 232px; bottom: 0;
    background: var(--card-black);
  }
  .contact-list {
    position: absolute; left: 44px; top: 258px;
    list-style: none;
    color: var(--text-light);
    font-size: 19px; line-height: 1.3;
  }
  .contact-list li { display: flex; align-items: flex-start; gap: 12px; margin-bottom: 4px; }
  .contact-list svg { width: 16px; height: 16px; margin-top: 4px; flex: none; fill: var(--text-light); }
</style>
</head>
<body>
<main class="canvas">
  <section class="card card-front" aria-label="Card front">
    <div class="wordmark"><span>Kestrel</span><span>Artists</span></div>
  </section>

  <section class="card card-back" aria-label="Card back">
    <div class="top-panel"></div>
    <div class="wordmark"><span>Kestrel</span><span>Artists</span></div>
    <div class="holder">
      <p class="holder-name">Employee Name</p>
      <p class="holder-role">Managing Director</p>
    </div>
    <div class="accent-stripe"></div>
    <div class="bottom-panel"></div>
    <ul class="contact-list">
      <li>
        <svg viewBox="0 0 16 16" aria-hidden="true"><circle cx="8" cy="4.5" r="3.5"/><path d="M1 16c0-4 3-6.5 7-6.5s7 2.5 7 6.5z"/></svg>
        <span>(+61 2) 5550 1742</span>
      </li>
      <li>
        <svg viewBox="0 0 16 16" aria-hidden="true"><path d="M1 3h14v10H1z M2 4l6 5 6-5" fill="none" stroke="#f2f2f2" stroke-width="1.6"/></svg>
        <span>info@kestrelartists.com.au</span>
      </li>
      <li>
        <svg viewBox="0 0 16 16" aria-hidden="true"><path d="M8 0a5.5 5.5 0 0 0-5.5 5.5C2.5 10 8 16 8 16s5.5-6 5.5-10.5A5.5 5.5 0 0 0 8 0zm0 7.8a2.3 2.3 0 1 1 0-4.6 2.3 2.3 0 0 1 0 4.6z"/></svg>
        <span>14 Harlow Lane, Redfern NSW 2016<br>Australia</span>
      </li>
    </ul>
  </section>
</main>
</body>
</html>
```